Maison Vurel

menu design, menu change,
will send hand written rough draft soon
Updates

Project Deadline Extended
Reason: Got off to a slow start. Things are progressing now. Thank you.

Target Market(s)

18-60 yr olds, blue collar & professionals, middle class, median income, families,upscale - casual- steakhouse concept

Industry/Entity Type

Restaurant

Colors
f68d4c
f37122
f78f20
faa54b
ffc214
fece3e
fbee3e
fbed22
333333

Requirements
Must have
• Front cover, back cover. 2 inside views
Nice to have
• 8 x 14 page size

```html
<!DOCTYPE html>
<html lang="en">
<head>
<meta charset="utf-8">
<title>Maison Vurel – Menu Inside Spread</title>
<link rel="stylesheet" href="https://fonts.googleapis.com/css2?family=Almendra+SC&family=Cinzel:wght@400;600&family=Open+Sans:ital,wght@0,600;1,400&display=swap">
<style>
  :root{
    --page-bg:#eef0f1;
    --panel:#4b4643;
    --panel-deep:#3a3634;
    --charcoal:#333333;
    --bar-yellow:#ffc214;
    --gold-text:#f2e25a;
    --line-orange:#f37122;
    --warm-orange:#f78f20;
    --soft-orange:#faa54b;
    --frame-yellow:#d8d13a;
    --ink:#1d1a17;
    --white:#ffffff;
  }
  *{box-sizing:border-box;margin:0;padding:0}
  html,body{width:1200px;height:1200px;overflow:hidden;background:var(--page-bg)}
  .canvas{position:relative;width:1200px;height:1200px}
  .menu{
    position:absolute;left:20px;top:122px;width:1262px;height:1040px;
    transform:scale(0.919);transform-origin:0 0;
    background:linear-gradient(160deg,var(--panel) 0%,var(--panel-deep) 100%);
    overflow:hidden;
    font-family:"Open Sans",sans-serif;color:var(--white);
  }
  .menu::after{
    content:"";position:absolute;left:638px;top:225px;bottom:10px;width:2px;
    background:linear-gradient(90deg,rgba(0,0,0,.25),rgba(255,255,255,.06));
  }
  .hero-band{
    position:absolute;left:0;top:0;width:100%;height:225px;
    background:
      radial-gradient(ellipse 200px 120px at 70px 120px,rgba(255,240,220,.35),transparent 70%),
      radial-gradient(ellipse 160px 130px at 840px 130px,rgba(255,245,230,.35),transparent 70%),
      radial-gradient(ellipse 170px 140px at 1160px 120px,rgba(60,10,10,.55),transparent 70%),
      radial-gradient(ellipse 420px 160px at 450px 90px,rgba(250,165,75,.8),transparent 70%),
      linear-gradient(180deg,#5a2a10 0%,#b45a1c 45%,#7a3612 100%);
    border-bottom:2px solid var(--line-orange);
  }
  .bottom-strip{position:absolute;left:0;bottom:0;width:100%;height:10px;background:var(--line-orange)}
  .brand{
    position:absolute;left:548px;top:170px;width:180px;height:130px;border-radius:50%;
    background:var(--ink);border:4px solid var(--warm-orange);
    display:flex;align-items:center;justify-content:center;text-align:center;z-index:2;
  }
  .brand-name{font-family:"Cinzel",serif;font-weight:600;font-size:22px;line-height:1.1;color:var(--bar-yellow)}
  .section-bar{
    position:absolute;height:48px;background:var(--bar-yellow);
    display:flex;align-items:center;justify-content:center;
    font-family:"Almendra SC",serif;font-size:40px;color:var(--ink);letter-spacing:1px;
  }
  .bar-burgers{left:0;top:256px;width:526px;border-radius:0 24px 24px 0}
  .bar-sandwiches{left:36px;top:484px;width:570px;border-radius:24px}
  .bar-cattle{left:30px;top:743px;width:580px;border-radius:24px}
  .bar-seafood{left:745px;top:253px;width:517px;border-radius:24px 0 0 24px;justify-content:flex-start;padding-left:10px}
  .section-note{
    position:absolute;font-family:"Cinzel",serif;font-size:16px;letter-spacing:1px;color:var(--white);
  }
  .section-note.italic{font-family:"Open Sans",sans-serif;font-style:italic;font-size:12px;letter-spacing:0}
  .item{position:absolute}
  .item-head{display:flex;justify-content:space-between;align-items:baseline;gap:6px}
  .item-name{font-family:"Cinzel",serif;font-size:12.5px;color:var(--gold-text);letter-spacing:.5px;white-space:nowrap}
  .price{font-weight:600;font-size:10.5px;color:var(--white)}
  .item-desc{font-style:italic;font-size:10.5px;line-height:1.35;color:var(--white)}
  .item-desc.small{font-size:8.5px}
  .food-photo{
    position:absolute;left:790px;top:598px;width:540px;height:185px;border-radius:50%;
    border-left:8px solid #111;
    background:
      radial-gradient(ellipse 120px 60px at 300px 100px,#f4c9a0,transparent 70%),
      radial-gradient(ellipse 260px 110px at 260px 95px,#c8501c,transparent 80%),
      linear-gradient(90deg,#7a2a0c,#d2641f 50%,#e8b44a);
  }
  .steak-box{
    position:absolute;left:656px;top:791px;width:590px;height:213px;
    border:1.5px solid var(--frame-yellow);background:rgba(40,36,34,.35);
  }
  .steak-title{
    position:absolute;left:0;right:0;top:14px;text-align:center;
    font-family:"Almendra SC",serif;font-size:26px;color:var(--white);letter-spacing:1px;
  }
  .steak-sub{position:absolute;left:0;right:0;text-align:center;font-style:italic;font-size:11px}
</style>
</head>
<body>
<div class="canvas">
  <div class="menu">
    <div class="hero-band" role="img" aria-label="Warm-lit restaurant table with water and wine glasses"></div>

    <div class="brand"><span class="brand-name">Maison<br>Vurel</span></div>

    <!-- Gourmet Burgers -->
    <div class="section-bar bar-burgers">Gourmet Burgers</div>
    <div class="section-note" style="left:188px;top:318px">All served with B...... Fries</div>

    <div class="item" style="left:32px;top:345px;width:285px">
      <div class="item-head"><span class="item-name">*Bacon Cheddar</span><span class="price">9.99</span></div>
      <p class="item-desc">Cheddar, Bacon and</p>
    </div>
    <div class="item" style="left:32px;top:382px;width:285px">
      <div class="item-head"><span class="item-name">*Great Western</span><span class="price">9.99</span></div>
      <p class="item-desc">Cheddar Cheese, Bacon, Onion Rings, and Hollan's BBQ Sauce!</p>
    </div>
    <div class="item" style="left:32px;top:428px;width:285px">
      <div class="item-head"><span class="item-name">*Ranch House Burger</span><span class="price">9.99</span></div>
      <p class="item-desc">Cheddar Cheese, Bacon, Onion Rings, and Fried egg</p>
    </div>
    <div class="item" style="left:383px;top:350px;width:225px">
      <div class="item-head"><span class="item-name">*Maison Vurel Burger</span><span class="price">9.99</span></div>
      <p class="item-desc small">Cheddar Cheese, Smoked Ham, more Cheese, Bacon</p>
    </div>
    <div class="item" style="left:383px;top:392px;width:225px">
      <div class="item-head"><span class="item-name">*Swiss Mushroom</span><span class="price">9.99</span></div>
      <p class="item-desc small">Swiss Cheese, Bacon</p>
    </div>
    <div class="item" style="left:383px;top:422px;width:225px">
      <div class="item-head"><span class="item-name">*Fire House Burger</span><span class="price">9.99</span></div>
      <p class="item-desc small">Pepper jack Cheese, Bacon, grilled onions, jalapenos &amp; Buffalo Sauce</p>
    </div>

    <!-- Signature Sandwiches -->
    <div class="section-bar bar-sandwiches">Signature Sandwiches</div>
    <div class="section-note" style="left:188px;top:541px">All served with B...... Fries</div>

    <div class="item" style="left:25px;top:576px;width:295px">
      <div class="item-head"><span class="item-name">Turkey Avocado Cream Cheese</span><span class="price">9.99</span></div>
      <p class="item-desc small" style="margin-top:14px;padding-left:18px">Smoked Turkey Avocados, Lettuce, Tomato, Cucumber, Cream Cheese, and Honey Mustard, on a Ciabatta Bun!</p>
    </div>
    <div class="item" style="left:25px;top:640px;width:295px">
      <div class="item-head"><span class="item-name">French Dip</span><span class="price">9.99</span></div>
      <p class="item-desc small">Slow roasted Beef, Cheese, Red Onion on a 12" Hoagie with Au Jus!</p>
    </div>
    <div class="item" style="left:25px;top:667px;width:295px">
      <div class="item-head"><span class="item-name">Classic Club House Sandwich</span><span class="price">9.99</span></div>
      <p class="item-desc small">Ham, Turkey, Cheese, Bacon, Lettuce, Tomato, Pickle, onion, Cheddar Cheese+ Swiss Cheese, 2 sauces in country style Bread Slices</p>
    </div>
    <div class="item" style="left:354px;top:576px;width:270px">
      <div class="item-head"><span class="item-name">Rueben</span><span class="price">8.99</span></div>
      <p class="item-desc small">Corned Beef, Swiss and Cheddar Cheese, Thousand Island Sauce in Grilled slice of Marble Rye!</p>
    </div>
    <div class="item" style="left:354px;top:621px;width:270px">
      <div class="item-head"><span class="item-name">Chicken Club Sandwich</span><span class="price">9.99</span></div>
      <p class="item-desc small">Hand Breaded Chicken Breast, Provolone Cheese, Bacon, Lettuce, Tomato, Pickle, all on a Brioche Bun!</p>
    </div>
    <div class="item" style="left:354px;top:666px;width:270px">
      <div class="item-head"><span class="item-name">Chicken Quesadilla</span><span class="price">8.99</span></div>
      <p class="item-desc small">Fajita Seasoned Chicken Breast Meat, Jack &amp; Cheddar, Cheese, all Grilled in a 12" Tortilla with Salsa and Sour Cream!</p>
    </div>

    <!-- Cattle Country -->
    <div class="section-bar bar-cattle">Catlle Country</div>
    <div class="section-note" style="left:148px;top:800px;font-size:13px">All seved with choice of Potato &amp;Hot Bread</div>

    <div class="item" style="left:25px;top:844px;width:235px">
      <div class="item-head"><span class="item-name">Steak Dei Rio</span><span class="price">12.99</span></div>
      <p class="item-desc">12oz choice tenderlon out rabbed with bold southwester spices, flame....... Tapped with chili pepper butter &amp; fried onion</p>
    </div>
    <div class="item" style="left:25px;top:918px;width:235px">
      <div class="item-head"><span class="item-name">Mushroom Ground Steak</span><span class="price">19.99</span></div>
      <p class="item-desc" style="white-space:nowrap">14oz ground......................with beef mushroom gravy</p>
    </div>
    <div class="item" style="left:25px;top:965px;width:235px">
      <div class="item-head"><span class="item-name">Chicken Fried Steak</span><span class="price">19.99</span></div>
      <p class="item-desc">Hand Breaded &amp; served with Country Gravy</p>
    </div>
    <div class="item" style="left:353px;top:839px;width:255px">
      <div class="item-head"><span class="item-name">Parmesian Proper Press Steak</span><span class="price">12.99</span></div>
      <p class="item-desc">12oz choice tenderlons cut, charboiled of coated with a parmesian Pepper crust</p>
    </div>
    <div class="item" style="left:353px;top:901px;width:255px">
      <div class="item-head"><span class="item-name">Steak Chateau Briand</span><span class="price">19.99</span></div>
      <p class="item-desc" style="width:280px">12oz choice tenderlon cut, drizzled with a parmesian sauce &amp; complimented with grilled aspapper spears.</p>
    </div>
    <div class="item" style="left:353px;top:962px;width:255px">
      <div class="item-head"><span class="item-name">Boston Bleau Heese Steak</span><span class="price">19.99</span></div>
      <p class="item-desc" style="width:280px">12oz choice tenderlon out rabbed with bold southwester spices, flame.......Topped with melting Bleu Cheese</p>
    </div>

    <!-- Chicken & Seafood -->
    <div class="section-bar bar-seafood">Chicken &amp; Seafood</div>
    <div class="section-note italic" style="left:812px;top:308px">served with choice of potato &amp; Hot Bread</div>

    <div class="item" style="left:679px;top:345px;width:252px">
      <div class="item-head"><span class="item-name">Carbo Chicken Breast</span><span class="price">14.99</span></div>
      <p class="item-desc">10oz Breast</p>
    </div>
    <div class="item" style="left:679px;top:408px;width:252px">
      <div class="item-head"><span class="item-name">Chicken Fried Chicken Breast</span><span class="price">14.99</span></div>
      <p class="item-desc" style="width:290px">10oz Hand Breaded Breast Fried, served with corn on the cab, mashed potatos Country Gravy</p>
    </div>
    <div class="item" style="left:679px;top:486px;width:270px">
      <div class="item-head"><span class="item-name">Hand Breaded Chicken Strips</span><span class="price">9.99</span></div>
      <p class="item-desc">Cut &amp; Bread per order</p>
    </div>
    <div class="item" style="left:679px;top:536px;width:252px">
      <div class="item-head"><span class="item-name">Chicken Ka-Bab</span><span class="price">19.99</span></div>
      <p class="item-desc" style="width:270px">10oz Charboiled Breast, with pappers onion, mushrooms, tomatos, Pineapple, and drizzeled with light...................</p>
    </div>
    <div class="item" style="left:973px;top:343px;width:250px">
      <div class="item-head"><span class="item-name">North Atlantic Salmon</span><span class="price">19.99</span></div>
      <p class="item-desc">Charboiled filet 8Oz</p>
    </div>
    <div class="item" style="left:973px;top:384px;width:250px">
      <div class="item-head"><span class="item-name">English Style Cod</span><span class="price">17.99</span></div>
      <p class="item-desc">House.......................................</p>
    </div>
    <div class="item" style="left:973px;top:423px;width:250px">
      <div class="item-head"><span class="item-name">Deep Fried Gulf Shrimp</span><span class="price">17.99</span></div>
      <p class="item-desc">Jumbo Shrimp</p>
    </div>
    <div class="item" style="left:973px;top:464px;width:250px">
      <div class="item-head"><span class="item-name">Mahi Mahi</span><span class="price">19.99</span></div>
      <p class="item-desc" style="width:190px">9Oz charboiled served under a shrimp &amp; mushroom white sauce on a ...... of steamed arden vegetabkes</p>
    </div>
    <div class="item" style="left:973px;top:554px;width:250px">
      <div class="item-head"><span class="item-name">Country Fried Catfish</span><span class="price">12.99</span></div>
      <p class="item-desc" style="white-space:nowrap">Catfish fillets, hand baked &amp; deep fried.</p>
    </div>

    <div class="food-photo" role="img" aria-label="Close-up of crispy fried chicken with fries"></div>

    <!-- Premium Steak Selections -->
    <div class="steak-box">
      <div class="steak-title">Maison Vurel Premium Steak Selections</div>
      <p class="steak-sub" style="top:56px">Choise and Prime Grade Beef</p>
      <p class="steak-sub" style="top:73px">served with House salad, choice of potato, and Hot Bread</p>

      <div class="item" style="left:24px;top:94px;width:192px">
        <div class="item-head"><span class="item-name">Filet Mignon</span></div>
        <p class="item-desc small" style="display:flex;justify-content:space-between">Becon Wrapped, the ........cut 8oz <b style="font-style:normal;font-size:10px">24.99</b></p>
        <p class="item-desc small" style="display:flex;justify-content:flex-end;gap:12px">10oz <b style="font-style:normal;font-size:10px">28.99</b></p>
      </div>
      <div class="item" style="left:24px;top:147px;width:192px">
        <div class="item-head"><span class="item-name">Kansas City Strip</span></div>
        <p class="item-desc small" style="display:flex;justify-content:space-between">Firmer texture, Full of Flavor 16oz <b style="font-style:normal;font-size:10px">26.99</b></p>
      </div>
      <div class="item" style="left:306px;top:98px;width:258px">
        <div class="item-head"><span class="item-name">*Ribeye Steak</span><span class="price">28.99</span></div>
        <p class="item-desc small" style="width:200px">Well .........rich, full of flavor cut from the prime rib 15oz</p>
      </div>
      <div class="item" style="left:306px;top:152px;width:258px">
        <div class="item-head"><span class="item-name">*Best Tenderlon Ka-Bab</span><span class="price">26.99</span></div>
        <p class="item-desc small">8oz beef tenderlon, ........with bell peppers, onions, tomatos, mushrooms, pineappl &amp; drizzeled with a light Italion........</p>
      </div>
    </div>

    <div class="bottom-strip"></div>
  </div>
</div>
</body>
</html>
```